Website for company called VORENTbio

We need a website for our new company called VORENTbio which developed a platform/technology to identify antigen-specific T cells (immune cells) which can be used for cancer therapy, autoimmunity, etc.

The platform is called VORENT and is rapid, versatile, unbiased, and inexpensive.

We have a semi-final logo although we are not completely set on color and font of text (attached).

Target Market(s)

Our target audience at the moment would be potential investors and VCs. We eventually are interested in getting attention from scientists and cell/immunotherapy companies.

Industry/Entity Type

Healthcare/Technology

Coding

Coded - Design and coding required

Number of Pages Required

1 page

Colors
0094D4
00A9DD
6FCCEA
C7EBF8
E9F6FB
00AB8E
00BBA5
67D7C9
C6EFE9
E9F9F6
E54698
E96AAD
F1A4CE
F9D9EA
FCEFF6
A7469A
B969AE
D3A5CF
EDDBEB
F8F0F9
6B429C
8869AF
B7A5CE
E3DAEB
F3F0F8

Requirements
Must have
• Landing page about the company, About us page, Technology page (could be merged with company landing page), Contact us page

```html
<!DOCTYPE html>
<html lang="en">
<head>
<meta charset="utf-8">
<title>VORENTbio — Antigen-Specific T Cell Discovery</title>
<link rel="stylesheet" href="https://fonts.googleapis.com/css2?family=IBM+Plex+Sans:wght@400;500;600;700&family=Inter:wght@400;500;600&display=swap">
<style>
:root{
  --teal:#00AB8E;
  --teal-2:#00BBA5;
  --blue:#0094D4;
  --blue-2:#00A9DD;
  --mint:#E9F9F6;
  --mint-2:#E6F6F4;
  --ink:#1E2528;
  --text:#5E6669;
  --line:#D9E3E5;
  --pink:#E54698;
  --violet:#6B429C;
  --white:#FFFFFF;
}
*{box-sizing:border-box;margin:0;padding:0}
html,body{width:1200px;height:4605px;overflow:hidden}
body{background:var(--mint);font-family:"Inter",sans-serif;color:var(--ink);position:relative}
.abs{position:absolute}
h1,h2,h3,h4,.heading{font-family:"IBM Plex Sans",sans-serif}
.btn{position:absolute;display:inline-flex;align-items:center;gap:14px;height:42px;padding:0 22px 0 26px;border-radius:22px;background:linear-gradient(90deg,var(--teal),var(--blue));color:#fff;font:600 14px "Inter",sans-serif;text-decoration:none;box-shadow:0 6px 14px rgba(0,148,212,.25)}
.btn svg{width:14px;height:14px}

/* header */
.site-header{position:absolute;top:0;left:0;width:1200px;height:89px;background:var(--mint)}
.brand{position:absolute;left:110px;top:18px;font:700 43px "IBM Plex Sans",sans-serif;color:var(--teal);letter-spacing:.5px}
.main-nav{position:absolute;left:453px;top:31px;display:flex;gap:49px;font-size:15px;color:var(--ink)}
.site-header .btn{left:928px;top:21px;height:44px}

/* hero */
.hero{position:absolute;top:89px;left:0;width:1200px;height:429px;background:radial-gradient(ellipse at 78% 50%,#7a5b4c 0%,#3d3a40 30%,#1e2530 60%,#141a22 100%)}
.hero h1{position:absolute;left:110px;top:106px;font:700 42px/52px "IBM Plex Sans",sans-serif;color:#fff;letter-spacing:.5px}
.hero p{position:absolute;left:110px;top:266px;font-size:17px;line-height:27px;color:#fff}
.hero .btn{left:110px;top:334px}
.dots{position:absolute;left:1141px;top:178px;display:flex;flex-direction:column;gap:9px}
.dots span{width:8px;height:8px;border-radius:50%;background:rgba(255,255,255,.4)}
.dots span:first-child{background:#fff}

/* about */
.about{position:absolute;left:111px;top:613px;width:1089px;height:871px;background:#fff}
.ph{position:absolute}
.about .ph-a{left:68px;top:74px;width:232px;height:280px;background:linear-gradient(135deg,#3b4a5c,#6f7d8c 50%,#b9777a)}
.about .ph-b{left:216px;top:214px;width:272px;height:256px;background:radial-gradient(circle at 55% 50%,#2f5e86,#5aa4c9 45%,#d25a8f 80%,#8dd0e8);box-shadow:0 10px 24px rgba(0,0,0,.2)}
.tag{position:absolute;left:323px;top:139px;border-left:2px solid var(--blue);padding-left:21px;height:48px;font:500 14px/21px "Inter",sans-serif;color:var(--ink)}
.tag::after{content:"";position:absolute;left:-2px;top:48px;height:34px;border-left:2px solid var(--line)}
.about h2{position:absolute;left:556px;top:72px;font:700 29px/42px "IBM Plex Sans",sans-serif;letter-spacing:.4px}
.about .copy{position:absolute;left:556px;top:218px;width:430px;padding-left:37px;border-left:2px solid var(--teal-2);font-size:13.5px;line-height:26px;color:var(--text)}
.about .copy p+p{margin-top:16px}
.about h3{position:absolute;left:0;width:978px;top:525px;text-align:center;font:600 26px "IBM Plex Sans",sans-serif}
.about .sub{position:absolute;left:0;width:978px;top:568px;text-align:center;font-size:15px;color:var(--text)}
.feature{position:absolute;top:620px;width:270px;text-align:center}
.feature .ico{width:78px;height:78px;border-radius:50%;margin:0 auto;background:linear-gradient(135deg,var(--teal-2),var(--blue));display:flex;align-items:center;justify-content:center;box-shadow:0 6px 14px rgba(0,148,212,.3)}
.feature .ico svg{width:40px;height:40px}
.feature h4{margin-top:22px;font:600 15px "IBM Plex Sans",sans-serif;letter-spacing:.5px}
.feature p{margin-top:8px;font-size:13.5px;line-height:23px;color:var(--text)}

/* growth */
.growth{position:absolute;left:0;top:1484px;width:1200px;height:1135px}
.growth h2{position:absolute;left:0;width:1200px;top:60px;text-align:center;font:600 29px/42px "IBM Plex Sans",sans-serif;letter-spacing:.5px}
.growth .sub{position:absolute;left:0;width:1200px;top:147px;text-align:center;font-size:15px;color:var(--text)}
.growth .video{left:193px;top:193px;width:814px;height:392px;background:radial-gradient(circle at 45% 55%,#f0a040 0%,#b04a6b 15%,#2f5f86 45%,#143048 100%)}
.play{position:absolute;left:26px;top:314px;width:54px;height:54px;border-radius:50%;background:#fff;display:flex;align-items:center;justify-content:center}
.growth .strand{left:0;top:590px;width:1200px;height:545px;background:linear-gradient(160deg,#dff2f4 0%,#bfe2ef 35%,#e9a5c2 55%,#9ccde6 75%,#6fa8cf 100%)}
.growth .lead{position:absolute;left:193px;top:622px;width:420px;font-size:15px;line-height:27px;color:var(--ink)}
.growth .btn{left:193px;top:755px}
.chat{position:absolute;left:1033px;top:1013px;width:54px;height:54px;border-radius:50%;background:#fff;display:flex;align-items:center;justify-content:center;box-shadow:0 4px 10px rgba(0,0,0,.15)}

/* platform */
.platform{position:absolute;left:0;top:2619px;width:1200px;height:739px;background:linear-gradient(180deg,#eef9f8,#e4f5f2)}
.platform h2{position:absolute;left:0;width:1200px;top:57px;text-align:center;font:600 29px "IBM Plex Sans",sans-serif;letter-spacing:.4px}
.platform .intro{position:absolute;left:200px;width:800px;top:105px;text-align:center;font-size:15px;line-height:26px;color:var(--text)}
.card{position:absolute;top:185px;width:234px;height:268px;background:#fff;border-top:3px solid;text-align:center;box-shadow:0 8px 20px rgba(0,0,0,.06)}
.card .ico{width:68px;height:68px;border-radius:50%;margin:30px auto 0;display:flex;align-items:center;justify-content:center}
.card .ico svg{width:34px;height:34px}
.card h4{margin-top:24px;font:600 16px "IBM Plex Sans",sans-serif;letter-spacing:.4px}
.card p{margin:6px 24px 0;font-size:13.5px;line-height:22px;color:var(--text)}
.platform .quote{position:absolute;left:150px;width:900px;top:516px;text-align:center;font:500 23px/37px "IBM Plex Sans",sans-serif}
.platform .btn{left:520px;top:643px}

/* partner */
.partner{position:absolute;left:0;top:3358px;width:1200px;height:1019px;background:linear-gradient(180deg,#fff 0%,#fff 55%,#d9ebf7 75%,#6ea4d6 100%)}
.partner .mesh{left:0;top:560px;width:1200px;height:459px;background:radial-gradient(ellipse at 15% 80%,#2f6fb8 0%,#6ea4d6 35%,rgba(200,225,245,.5) 70%,rgba(255,255,255,0) 100%)}
.partner h2{position:absolute;left:0;width:1200px;top:50px;text-align:center;font:600 29px/42px "IBM Plex Sans",sans-serif;letter-spacing:.4px}
.partner .intro{position:absolute;left:240px;width:720px;top:146px;text-align:center;font-size:15px;line-height:27px;color:var(--text)}
.partner .pic{left:206px;top:289px;width:393px;height:398px;border:4px solid #fff;background:linear-gradient(140deg,#a7466b,#d8738f 35%,#5b6e9c 65%,#2f4f7c);box-shadow:0 10px 24px rgba(0,0,0,.15)}
.partner h3{position:absolute;left:656px;top:295px;width:430px;font:600 20px/33px "IBM Plex Sans",sans-serif}
.point{position:absolute;left:656px;width:440px}
.point h4{font:600 14px "IBM Plex Sans",sans-serif;color:var(--blue);padding-left:31px;position:relative;letter-spacing:.3px}
.point h4 svg{position:absolute;left:0;top:0;width:15px;height:15px}
.point p{margin-top:12px;padding-left:31px;font-size:13.5px;line-height:24px;color:var(--text)}
.partner .btn{left:656px;top:612px}

/* footer */
.site-footer{position:absolute;left:0;top:4377px;width:1200px;height:228px;background:#fff}
.site-footer .brand{top:36px;left:108px}
.social{position:absolute;left:966px;top:55px;display:flex;gap:11px}
.social span{width:34px;height:34px;border-radius:50%;background:linear-gradient(135deg,var(--teal),var(--blue))}
.foot-nav{position:absolute;left:108px;top:119px;width:983px;border-top:1px solid var(--line);padding-top:19px;display:flex;justify-content:space-between;font:500 16px "IBM Plex Sans",sans-serif;letter-spacing:.4px}
.legal{position:absolute;left:108px;top:180px;width:983px;font-size:11px;color:var(--text);display:flex;justify-content:space-between}
.legal .links span+span{margin-left:22px;padding-left:22px;border-left:1px solid var(--line)}
</style>
</head>
<body>

<header class="site-header">
  <div class="brand">VORENTbio</div>
  <nav class="main-nav"><span>Home</span><span>About Us</span><span>Technology</span><span>Case Studies</span></nav>
  <a class="btn" href="#contact">Contact Us <svg viewBox="0 0 16 16"><circle cx="8" cy="8" r="8" fill="#fff"/><path d="M6 4.5 9.5 8 6 11.5" stroke="#0094D4" stroke-width="2" fill="none"/></svg></a>
</header>

<section class="hero" role="img" aria-label="Close-up of an immune cell being approached by a glowing injection needle">
  <h1>REVOLUTIONIZING<br>T CELL DISCOVERY FOR<br>NEXT-GEN THERAPIES</h1>
  <p>Powering the future of cancer, infectious disease, and<br>autoimmune therapies with speed, precision, &amp; scale.</p>
  <a class="btn" href="#tech">About VORENT Technology <svg viewBox="0 0 16 16"><circle cx="8" cy="8" r="8" fill="#fff"/><path d="M6 4.5 9.5 8 6 11.5" stroke="#0094D4" stroke-width="2" fill="none"/></svg></a>
  <div class="dots"><span></span><span></span><span></span><span></span></div>
</section>

<section class="about">
  <div class="ph ph-a" role="img" aria-label="Microscope view of a cell receiving a pipette injection"></div>
  <div class="ph ph-b" role="img" aria-label="Illustration of a virus particle surrounded by immune cells"></div>
  <div class="tag">Adoptive T Cell<br>Therapies</div>
  <h2>PIONEERING THE FUTURE OF<br>ANTIGEN-SPECIFIC T CELL<br>DISCOVERY</h2>
  <div class="copy">
    <p>VORENTbio is a biotechnology company founded to unlock the therapeutic potential of the immune system. With our proprietary VORENT platform, we identify rare antigen-specific T cells with unprecedented accuracy, transforming how the world approaches precision immunotherapy.</p>
    <p>To empower researchers, clinicians, and developers with powerful, accessible tools to accelerate T cell-based discovery and therapies.</p>
  </div>
  <h3>Building the Next Generation of Immune Diagnostics.</h3>
  <div class="sub">Revolutionizing Immunotherapy Through Precision Science.</div>
  <div class="feature" style="left:46px">
    <div class="ico"><svg viewBox="0 0 40 40" fill="none" stroke="#fff" stroke-width="2"><path d="M8 26c4 0 6 4 12 4s8-4 12-4M20 8c-5 4-5 10 0 14 5-4 5-10 0-14z"/></svg></div>
    <h4>ANTIGEN-AGNOSTIC PRECISION</h4>
    <p>Sed ut perspiciatis unde omnis iste natus error sit voluptatem accusantium doloremque laudantium</p>
  </div>
  <div class="feature" style="left:353px">
    <div class="ico"><svg viewBox="0 0 40 40" fill="none" stroke="#fff" stroke-width="2"><circle cx="20" cy="20" r="8"/><path d="M20 5v7M20 28v7M5 20h7M28 20h7M9 9l5 5M26 26l5 5M31 9l-5 5M14 26l-5 5"/></svg></div>
    <h4>THERAPEUTIC APPLICATIONS</h4>
    <p>Sed ut perspiciatis unde omnis iste natus error sit voluptatem accusantium doloremque laudantium</p>
  </div>
  <div class="feature" style="left:664px">
    <div class="ico"><svg viewBox="0 0 40 40" fill="none" stroke="#fff" stroke-width="2"><circle cx="20" cy="16" r="8"/><path d="M6 30c6 0 8 4 14 4s8-4 14-4M17 16h6M20 13v6"/></svg></div>
    <h4>FASTER + MORE ACCESSIBLE</h4>
    <p>Sed ut perspiciatis unde omnis iste natus error sit voluptatem accusantium doloremque laudantium</p>
  </div>
</section>

<section class="growth">
  <h2>WHERE BREAKTHROUGH SCIENCE MEETS<br>STRATEGIC GROWTH</h2>
  <div class="sub">Empowering Precision Medicine Through VORENT Technology</div>
  <div class="ph strand" role="img" aria-label="Pink and blue molecular strand illustration"></div>
  <div class="ph video" role="img" aria-label="Video still of T cells attacking a tumor cell">
    <div class="play"><svg width="16" height="16" viewBox="0 0 16 16"><path d="M4 2l10 6-10 6z" fill="#00AB8E"/></svg></div>
  </div>
  <p class="lead">Sed ut perspiciatis unde omnis iste natus error sit voluptatem accusantium doloremque laudantium, totam rem aperiam, eaque ipsa quae ab illo inventore veritatis et quasi architecto beatae vitae</p>
  <a class="btn" href="#contact">Contact Us <svg viewBox="0 0 16 16"><circle cx="8" cy="8" r="8" fill="#fff"/><path d="M6 4.5 9.5 8 6 11.5" stroke="#0094D4" stroke-width="2" fill="none"/></svg></a>
  <div class="chat"><svg width="22" height="20" viewBox="0 0 22 20"><path d="M2 4a3 3 0 0 1 3-3h10a3 3 0 0 1 3 3v6a3 3 0 0 1-3 3H8l-4 3v-3a3 3 0 0 1-2-3z" fill="#00AB8E"/></svg></div>
</section>

<section class="platform" id="tech">
  <h2>THE VORENT PLATFORM TECHNOLOGY</h2>
  <p class="intro">VORENT is a high-throughput, antigen-agnostic method that enables the direct discovery of functional, antigen-specific T cells. Unlike current approaches, VORENT is designed to be:</p>
  <div class="card" style="left:111px;border-color:var(--blue)">
    <div class="ico" style="background:linear-gradient(135deg,#00A9DD,#0094D4)"><svg viewBox="0 0 34 34" fill="none" stroke="#fff" stroke-width="2"><path d="M17 5c-5 4-5 10 0 14 5-4 5-10 0-14zM7 24c4 0 5 3 10 3s6-3 10-3"/></svg></div>
    <h4>UNBIASED</h4>
    <p>Sed ut perspiciatis unde omn is iste natus error sit volupt at em accusantium doloremque laudantium</p>
  </div>
  <div class="card" style="left:359px;border-color:var(--teal)">
    <div class="ico" style="background:linear-gradient(135deg,#00BBA5,#00AB8E)"><svg viewBox="0 0 34 34" fill="none" stroke="#fff" stroke-width="2"><rect x="6" y="8" width="22" height="16" rx="2"/><path d="M11 28h12M10 19l4-4 3 3 6-6"/></svg></div>
    <h4>RAPID</h4>
    <p>Sed ut perspiciatis unde omn is iste natus error sit volupt at em accusantium doloremque laudantium</p>
  </div>
  <div class="card" style="left:608px;border-color:var(--pink)">
    <div class="ico" style="background:linear-gradient(135deg,#E96AAD,#E54698)"><svg viewBox="0 0 34 34" fill="none" stroke="#fff" stroke-width="2"><circle cx="17" cy="17" r="6"/><path d="M17 5v5M17 24v5M5 17h5M24 17h5M9 9l3 3M22 22l3 3M25 9l-3 3M12 22l-3 3"/></svg></div>
    <h4>VERSATILE</h4>
    <p>Sed ut perspiciatis unde omn is iste natus error sit volupt at em accusantium doloremque laudantium</p>
  </div>
  <div class="card" style="left:855px;border-color:var(--violet)">
    <div class="ico" style="background:linear-gradient(135deg,#8869AF,#6B429C)"><svg viewBox="0 0 34 34" fill="none" stroke="#fff" stroke-width="2"><circle cx="17" cy="13" r="7"/><path d="M5 26c5 0 7 3 12 3s7-3 12-3M15 13h4M17 11v4"/></svg></div>
    <h4>COST-EFFICIENT</h4>
    <p>Sed ut perspiciatis unde omn is iste natus error sit volupt at em accusantium doloremque laudantium</p>
  </div>
  <p class="quote">T cell-based therapies are only as good as the tools used to discover them. VORENT brings a paradigm shift — from fishing in the dark to mapping immune responses in full clarity.</p>
  <a class="btn" href="#contact">Contact Us <svg viewBox="0 0 16 16"><circle cx="8" cy="8" r="8" fill="#fff"/><path d="M6 4.5 9.5 8 6 11.5" stroke="#0094D4" stroke-width="2" fill="none"/></svg></a>
</section>

<section class="partner" id="contact">
  <div class="ph mesh" role="img" aria-label="Blue virus particle illustration with flowing mesh lines"></div>
  <h2>INTERESTED IN PARTNERING OR INVESTING<br>IN VORENTBIO?</h2>
  <p class="intro">Sed ut perspiciatis unde omnis iste natus error sit voluptatem accusantium doloremque laudantium, totam rem aperiam, eaque ipsa quae ab illo inventore veritatis et quasi architecto beatae vitae dicta sunt explicabo. Nemo enim ipsam voluptatem quia voluptas sit aspernatur aut odit aut fugit, sed quia consequuntur magni dolores</p>
  <div class="ph pic" role="img" aria-label="Illustration of T cells and pathogens in a pink and blue environment"></div>
  <h3>A rapid, scalable, &amp; affordable platform for next-generation immunotherapies.</h3>
  <div class="point" style="top:388px">
    <h4><svg viewBox="0 0 15 15"><rect width="15" height="15" rx="2" fill="#0094D4"/><path d="M3.5 7.5l3 3 5-6" stroke="#fff" stroke-width="2" fill="none"/></svg>CELL THERAPY DEVELOPMENT</h4>
    <p>Sed ut perspiciatis unde omnis iste natus error sit voluptatem accusantium doloremque laudantium, totam rem aperiam, eaque ipsa quae ab illo inventore veritatis</p>
  </div>
  <div class="point" style="top:508px">
    <h4><svg viewBox="0 0 15 15"><rect width="15" height="15" rx="2" fill="#0094D4"/><path d="M3.5 7.5l3 3 5-6" stroke="#fff" stroke-width="2" fill="none"/></svg>TUMOR/PATHOGEN T CELL DISCOVERY</h4>
    <p>Sed ut perspiciatis unde omnis iste natus error sit voluptatem accusantium doloremque laudantium, totam rem aperiam, eaque ipsa quae ab illo inventore veritatis</p>
  </div>
  <a class="btn" href="#contact">Contact Us <svg viewBox="0 0 16 16"><circle cx="8" cy="8" r="8" fill="#fff"/><path d="M6 4.5 9.5 8 6 11.5" stroke="#0094D4" stroke-width="2" fill="none"/></svg></a>
</section>

<footer class="site-footer">
  <div class="brand">VORENTbio</div>
  <div class="social" aria-label="Social links"><span></span><span></span><span></span></div>
  <nav class="foot-nav"><span>HOME</span><span>ABOUT US</span><span>SERVICES</span><span>TECHNOLOGY</span><span>CASE STUDIES</span><span>TESTIMONIALS</span><span>CONTACT US</span></nav>
  <div class="legal"><span>(C) Copyright | All Rights Reserved</span><span class="links"><span>Terms &amp; Conditions</span><span>Privacy Policy</span></span></div>
</footer>

</body>
</html>
```